Business Card Design

General Brief:
Verant Works is a newly established international manufacturing company. We have a manufacturing facility in China and are in the process of building a new facility in Brazil and are expanding into Africa, the Middle East and Western markets by marketing our products through a licensee program. We use production line manufacture processes (similar to the automotive industry) to produce houses, apartments, hotels and accommodation for the resource sector. We will need to be able to differentiate between the various regions that we serve and the market we operate in.

Key Words to describe our business:
International, Global, Professional, Quality, Standard Compliant, Designful, Cost Effective, Experienced

General Brief:
We need business card designs which cater for the possibility of differentiating the various regions that we serve and the market we operate in. Also, we need a secondary typography selection which suits the primary typography used in the corporate signature (please always state which font is being applied so as to cross-check for the necessary font licenses). First print will be made for our Chinese head office and division, therefore will have the special prerequisite of featuring two distinct languages: English-speaking and Chinese. We assume that a double sided version (recto/verso) could work best in order to separate the languages—other creative interpretations, options and integrations are welcome.

Logo Symbolism:
A dot might seem to be an unassuming little thing, the first mark on the pristine sheet of paper. In this case, the dot is a beginning. But see what just happened there? The dot, an essential component in the structure of the sentence, closed it, making it a symbol of ending. Therefore, the dot is both an origination and a conclusion, encompassing all the possibilities of the universe within it, a seed full of potential and a symbol of the supreme being. The dot is also called the "bindhu," which means "drop." The bindhu is a symbol of the absolute, marked on the forehead at the position of the third eye in the place believed to be the seat of the soul. The presence of dots outside or within a symbol can signify the presence of something else. It also acts as reminder of the concept of space and all in all performs as a very positive symbol in the Verant Works logo.
Updates

Target Market(s)

See Stationary Project

Industry/Entity Type

Accommodation

Requirements
Must have
• See Stationary Project

Logo on Stationary Project

Files

```html
<!DOCTYPE html>
<html lang="en">
<head>
<meta charset="utf-8">
<title>Verant Works – Business Card</title>
<link rel="stylesheet" href="https://fonts.googleapis.com/css2?family=Montserrat:wght@700&family=Questrial&family=Noto+Sans+SC:wght@400;700&display=swap">
<style>
  :root {
    --page-bg: #e6e7e9;
    --card-bg: #f7f7f7;
    --navy: #0f2a3a;
    --accent-blue: #2a8fd0;
    --text-dark: #1f3442;
    --band-grey: #6b6f78;
    --band-navy: #0d2632;
  }
  * { box-sizing: border-box; margin: 0; padding: 0; }
  html, body {
    width: 1200px; height: 1000px; overflow: hidden;
    background: var(--page-bg);
  }
  .card {
    position: absolute; left: 240px;
    width: 720px; height: 412px;
    background: var(--card-bg);
    border-radius: 19px;
    overflow: hidden;
    font-family: "Questrial", "Century Gothic", sans-serif;
    color: var(--text-dark);
    box-shadow: 0 6px 18px rgba(0,0,0,0.12);
  }
  .card-english { top: 58px; }
  .card-chinese { top: 530px; }
  .card-chinese .address,
  .card-chinese .person-role { font-family: "Noto Sans SC", "Questrial", sans-serif; }
  .card-chinese .person-name { font-family: "Noto Sans SC", "Montserrat", sans-serif; letter-spacing: 2px; }

  .brand {
    position: absolute; left: 50px; top: 84px;
    font-size: 53px; line-height: 1; color: var(--navy);
    letter-spacing: -0.4px; white-space: nowrap;
  }
  .person { position: absolute; right: 50px; top: 90px; text-align: right; }
  .person-name {
    font-family: "Montserrat", "Century Gothic", sans-serif;
    font-weight: 700; font-size: 22px; color: var(--navy); line-height: 1.15;
  }
  .person-role { font-size: 18px; color: var(--text-dark); line-height: 1.3; }

  .contact {
    position: absolute; top: 304px; left: 0; width: 100%;
    font-size: 17.6px; line-height: 27px;
  }
  .address { position: absolute; right: 468px; text-align: right; white-space: nowrap; }
  .contact-col { position: absolute; }
  .contact-col.web { left: 286px; }
  .contact-col.phone { left: 510px; }
  .contact-line { display: flex; align-items: center; gap: 10px; white-space: nowrap; }
  .contact-line svg { width: 18px; height: 18px; flex: none; }

  .band { position: absolute; left: 0; bottom: 0; width: 100%; height: 30px; display: flex; }
  .band-grey { width: 270px; background: var(--band-grey); }
  .band-gap { width: 3px; background: var(--card-bg); }
  .band-navy { flex: 1; background: var(--band-navy); }
</style>
</head>
<body>
  <svg width="0" height="0" style="position:absolute" aria-hidden="true">
    <defs>
      <symbol id="icon-mail" viewBox="0 0 22 22">
        <circle cx="11" cy="11" r="10" fill="none" stroke="#2a8fd0" stroke-width="1.6"/>
        <rect x="5.5" y="7.5" width="11" height="7" rx="1" fill="#2a8fd0"/>
        <path d="M5.5 8 L11 12 L16.5 8" fill="none" stroke="#fff" stroke-width="1.1"/>
      </symbol>
      <symbol id="icon-web" viewBox="0 0 22 22">
        <g fill="none" stroke="#2a8fd0" stroke-width="1.6">
          <circle cx="11" cy="11" r="9.5"/>
          <ellipse cx="11" cy="11" rx="4.2" ry="9.5"/>
          <line x1="1.5" y1="11" x2="20.5" y2="11"/>
          <path d="M3.5 6.5 H18.5 M3.5 15.5 H18.5"/>
        </g>
      </symbol>
      <symbol id="icon-phone" viewBox="0 0 22 22">
        <circle cx="11" cy="11" r="10" fill="none" stroke="#2a8fd0" stroke-width="1.6"/>
        <path d="M7.5 5.5 L9.5 5.5 L10.5 8.5 L9 9.8 C9.8 11.6 10.6 12.5 12.3 13.2 L13.6 11.7 L16.5 12.7 L16.5 14.7 C16.5 15.6 15.6 16.4 14.6 16.2 C10.2 15.4 6.8 12 6 7.6 C5.8 6.5 6.5 5.5 7.5 5.5 Z" fill="#2a8fd0"/>
      </symbol>
      <symbol id="icon-fax" viewBox="0 0 22 22">
        <circle cx="11" cy="11" r="10" fill="none" stroke="#2a8fd0" stroke-width="1.6"/>
        <rect x="7.5" y="5" width="7" height="4" fill="#2a8fd0"/>
        <rect x="5" y="9" width="12" height="6" rx="1" fill="#2a8fd0"/>
        <rect x="7.5" y="13" width="7" height="4" fill="#fff" stroke="#2a8fd0" stroke-width="1"/>
      </symbol>
    </defs>
  </svg>

  <div class="card card-english" lang="en">
    <div class="brand">Verant Works</div>
    <div class="person">
      <div class="person-name">MARA ELLISON</div>
      <div class="person-role">Manager</div>
    </div>
    <div class="contact">
      <div class="address">
        <div>Harlow Park Road</div>
        <div>Westfield Vale NSW 2199</div>
      </div>
      <div class="contact-col web">
        <div class="contact-line"><svg><use href="#icon-mail"/></svg><span>info@verantworks.com</span></div>
        <div class="contact-line"><svg><use href="#icon-web"/></svg><span>www.verantworks.com</span></div>
      </div>
      <div class="contact-col phone">
        <div class="contact-line"><svg><use href="#icon-phone"/></svg><span>+61 2 5550 1400</span></div>
        <div class="contact-line"><svg><use href="#icon-fax"/></svg><span>+61 2 5550 1410</span></div>
      </div>
    </div>
    <div class="band"><div class="band-grey"></div><div class="band-gap"></div><div class="band-navy"></div></div>
  </div>

  <div class="card card-chinese" lang="zh-Hans">
    <div class="brand">Verant Works</div>
    <div class="person">
      <div class="person-name">马拉·埃利森</div>
      <div class="person-role">经理</div>
    </div>
    <div class="contact">
      <div class="address">
        <div>哈洛公园路</div>
        <div>新州韦斯特菲尔德谷 2199</div>
      </div>
      <div class="contact-col web">
        <div class="contact-line"><svg><use href="#icon-mail"/></svg><span>info@verantworks.com</span></div>
        <div class="contact-line"><svg><use href="#icon-web"/></svg><span>www.verantworks.com</span></div>
      </div>
      <div class="contact-col phone">
        <div class="contact-line"><svg><use href="#icon-phone"/></svg><span>+61 2 5550 1400</span></div>
        <div class="contact-line"><svg><use href="#icon-fax"/></svg><span>+61 2 5550 1410</span></div>
      </div>
    </div>
    <div class="band"><div class="band-grey"></div><div class="band-gap"></div><div class="band-navy"></div></div>
  </div>
</body>
</html>
```